Super-fantastic-interesting infographic of terribly boring content

-Looking to provide a visually engaging snapshot of the average Canadian investor.
-Help people compare their personal financial situation against the infographic (Average).
-We want viewers to feel engaged and interested in the info presented, not confused and irritated.

Data points to present:

The average Canadian snapshot:
* Average Canadian household Income in 2016: $76,900
* Median Net Worth of Canadian families in 2016: $295,100
* Average annual household expenditures on goods a& services: $62,183
* Median value in principal residence: $349,000
* Highest net annual savings amount (Age 35-44): $10,120
* Number of Canadian families holding a mortgage: 38.4%
* Median Mortgage value of Principal residence: $190,000
* Debt to disposable income ratio average: 172.1
* Total value of all assets held by Canadians in 2016: 12 Trillion dollars
* The principal residence was the single largest asset held (of the 12 Trillion): 32%
* Private pensions was the 2nd largest grouping of assets at 29.2%
* The average borrowing rate for Canadian mortgages: 2.94%
* 74% were fixed rate, 21% were variable and 5% blended.
* 48% of Canadians do not save or invest at all
* 54% of Canadians do not budget regularly
* 1 in 3 Canadians have lost at least 20% in one year
* 51% of Canadians took NO ACTION after losing at least 20% in one year.
* 22% of those people either, hired or fired an advisor

Financial advice landscape:
* # of households in Canada: 13,300,000
* Households with an advisor 5,300,000
* % of households dissatisfied with existing advisor 1,100,000

Target Market(s)

Investors, ages 22-55

Industry/Entity Type

Financial

Font styles to use
Sans Serif

Colors

Designer to choose colors to be used in the design.

Requirements
Must have
• Header: Financial landscape of the average Canadian
Nice to have
• There is a lot of numbers and percentages, find a way to deliver the info using a mix of images, numbers, pictures etc.

```html
<!DOCTYPE html>
<html lang="en">
<head>
<meta charset="utf-8">
<title>The Average Canadian Snapshot</title>
<link href="https://fonts.googleapis.com/css2?family=Anton&family=Oswald:wght@400;500;600&family=Luckiest+Guy&family=Alfa+Slab+One&display=swap" rel="stylesheet">
<style>
:root{
  --red:#e3212b;
  --pink:#f79c9c;
  --salmon:#f69696;
  --ink:#141428;
  --wine:#9a0f14;
  --blue:#2a1cff;
  --teal:#7fcfcf;
  --teal-soft:#6cc6c9;
  --green:#86c99c;
  --yellow:#ffe94a;
  --white:#ffffff;
}
*{margin:0;padding:0;box-sizing:border-box}
html,body{width:1200px;height:3000px;overflow:hidden;background:var(--white)}
body{font-family:"Oswald",sans-serif;color:var(--ink)}
.canvas{position:relative;width:1200px;height:3000px;overflow:hidden}
.abs{position:absolute}
.num{font-family:"Anton",sans-serif;color:var(--wine);line-height:1}
.head{font-family:"Anton",sans-serif;color:var(--ink);line-height:1}

/* header */
.masthead{left:0;top:0;width:1200px;height:110px;background:linear-gradient(180deg,#c9141d 0%,#ef3a3f 45%,#f46a6a 100%)}
.masthead h1{position:absolute;left:0;top:18px;width:1200px;text-align:center;font-family:"Anton",sans-serif;font-weight:400;font-size:82px;letter-spacing:1px;color:var(--ink);-webkit-text-stroke:2px var(--white);paint-order:stroke fill;line-height:1}

/* income */
.budget{left:0;top:110px;width:1200px;height:460px;background:var(--pink)}
.leaf-art{left:260px;top:0;width:700px;height:460px;background:radial-gradient(ellipse at 50% 55%,#fde0e0 0%,#fbcaca 55%,rgba(251,202,202,0) 80%)}
.budget-tag{font-family:"Luckiest Guy","Anton",sans-serif;font-size:46px;color:var(--yellow);-webkit-text-stroke:3px var(--ink);paint-order:stroke fill;letter-spacing:1px;line-height:1}
.budget-label{width:380px;text-align:right;font-size:28px;line-height:1;font-weight:500}
.bar{left:700px;width:200px;height:44px;border:5px solid #333;border-radius:8px;background:linear-gradient(180deg,#fff,#ddd);overflow:hidden}
.bar span{display:block;height:100%}
.budget-value{left:912px;font-size:54px}

/* family */
.family{left:0;top:570px;width:1200px;height:280px;background:var(--salmon)}
.section-title{font-family:"Anton",sans-serif;font-size:70px;color:var(--ink);line-height:1}
.rule{height:4px;background:var(--ink)}
.stat-line{font-size:30px;font-weight:500;line-height:1}
.family-icon{left:866px;top:620px;width:160px;height:170px;background:linear-gradient(180deg,#2a2a2a,#111);border-radius:80px 80px 16px 16px}

/* assets */
.total-value{left:0;top:900px;width:1200px;text-align:center;font-family:"Anton",sans-serif;font-size:56px;color:#c4121a;-webkit-text-stroke:4px var(--yellow);paint-order:stroke fill;line-height:1}
.total-caption{left:0;top:972px;width:1200px;text-align:center;font-size:30px;line-height:1}
.rank{font-family:"Alfa Slab One",serif;font-size:54px;color:var(--ink);line-height:1;z-index:3}
.rank-tag{background:var(--yellow);font-size:28px;padding:2px 8px;line-height:1.1;font-weight:500;z-index:3}
.frame{border:7px solid var(--teal);border-radius:22px;background:var(--white)}
.disc{border-radius:50%;background:var(--teal-soft)}
.disc-label{font-family:"Anton",sans-serif;font-size:44px;color:var(--ink);text-align:center;line-height:1.2}
.pct-disc{border-radius:50%;background:var(--green);display:flex;align-items:center;justify-content:center;font-family:"Anton",sans-serif;color:var(--wine);font-size:52px}
.icon-ph{background:#222;border-radius:12px}
.blue{color:var(--blue)}
.detail{font-size:32px;line-height:1.05;font-weight:500}
.habit{display:flex;align-items:center;gap:14px}
.habit .num{font-size:80px}
.habit p{font-size:30px;line-height:1}

/* debts */
.debts{left:0;top:1720px;width:1200px;height:300px;background:var(--salmon)}
.divider{background:rgba(255,255,255,.7)}
.borrow-label{font-size:24px;font-weight:500;line-height:1}
.borrow-bar{height:26px;background:var(--teal)}
.borrow-pct{font-size:22px;line-height:1}

/* losses */
.people-icons{left:96px;top:2046px;width:220px;height:160px;background:linear-gradient(90deg,#67c9dc 0 33%,#8f8f8f 33% 100%);border-radius:40px 40px 6px 6px}
.loss-text{font-size:32px;line-height:1}
.loss-row{display:flex;align-items:center;gap:16px}
.loss-row .num{font-size:80px;flex:none}

/* advice */
.advice{left:0;top:2370px;width:1200px;height:630px;background:var(--salmon)}
.advice-foot{left:0;top:2920px;width:1200px;height:80px;background:var(--red)}
.advisor-art{left:0;top:2380px;width:430px;height:540px;background:linear-gradient(180deg,#e23038 0%,#c5282e 30%,#1f2a44 60%,#2b2f3e 100%)}
.advice-label{font-size:32px;font-weight:500;line-height:1}
.advice-value{font-family:"Anton",sans-serif;font-size:46px;line-height:1;color:var(--ink)}
.brand{left:890px;top:2942px;display:flex;align-items:center;gap:10px;font-family:"Oswald",sans-serif;font-size:30px;font-weight:500;color:#2c3a66}
.brand i{display:block;width:30px;height:30px;border-radius:50%;background:#2c3a66}
</style>
</head>
<body>
<main class="canvas">

  <header class="abs masthead"><h1>THE AVERAGE CANADIAN SNAPSHOT</h1></header>

  <section class="abs budget" aria-label="Income, expenses and savings">
    <div class="abs leaf-art" role="img" aria-label="Large pale maple leaf backdrop"></div>

    <div class="abs budget-tag" style="left:124px;top:82px">INCOME</div>
    <div class="abs budget-label" style="left:304px;top:94px">Household income :</div>
    <div class="abs bar" style="top:88px"><span style="width:86%;background:linear-gradient(180deg,#6d88d8,#3a5bb8)"></span></div>
    <div class="abs num budget-value" style="top:82px">$76,900</div>

    <div class="abs budget-tag" style="left:124px;top:176px">EXPENSES</div>
    <div class="abs budget-label" style="left:304px;top:146px;line-height:1.05">Average annual<br>household expenditure<br>on goods &amp; services:</div>
    <div class="abs bar" style="top:182px"><span style="width:70%;background:linear-gradient(180deg,#ff8a3a,#e85a0c)"></span></div>
    <div class="abs num budget-value" style="top:176px">$62,183</div>

    <div class="abs budget-tag" style="left:124px;top:278px">SAVINGS</div>
    <div class="abs budget-label" style="left:304px;top:282px;line-height:1.05">Highest net annual<br>savings amount<br>(age 35-44) :</div>
    <div class="abs bar" style="top:290px"><span style="width:14%;background:linear-gradient(180deg,#fff68a,#f2dc2a)"></span></div>
    <div class="abs num budget-value" style="top:284px">$10,120</div>
  </section>

  <section class="abs family" aria-label="Canadian family"></section>
  <h2 class="abs section-title" style="left:76px;top:596px">CANADIAN FAMILY</h2>
  <div class="abs rule" style="left:76px;top:670px;width:460px"></div>
  <p class="abs stat-line" style="left:76px;top:690px">Median Net Worth of Canadian families :</p>
  <div class="abs num" style="left:582px;top:670px;font-size:58px">$295,100</div>
  <p class="abs" style="left:76px;top:726px;font-size:18px;font-weight:500">(in 2016)</p>
  <p class="abs stat-line" style="left:76px;top:772px">Numbers of Canadian families holding a mortgage :</p>
  <div class="abs num" style="left:696px;top:764px;font-size:46px">38.4%</div>
  <div class="abs family-icon" role="img" aria-label="Silhouette of a family with a child"></div>

  <h2 class="abs section-title" style="left:52px;top:876px;font-size:64px">ASSET</h2>
  <div class="abs rule" style="left:52px;top:946px;width:150px;height:3px"></div>
  <div class="abs total-value">12 Trillion dollars</div>
  <p class="abs total-caption">Total value of all assets held by canadians</p>

  <svg class="abs" style="left:180px;top:930px" width="840" height="190" viewBox="0 0 840 190" aria-hidden="true">
    <path d="M210 20 Q110 30 90 130" fill="none" stroke="#c8131b" stroke-width="26"/>
    <polygon points="50,120 140,120 92,185" fill="#c8131b"/>
    <path d="M630 20 Q730 30 750 110" fill="none" stroke="#c8131b" stroke-width="26"/>
    <polygon points="700,100 800,100 752,165" fill="#c8131b"/>
  </svg>

  <div class="abs frame" style="left:30px;top:1160px;width:556px;height:540px"></div>
  <div class="abs disc" style="left:70px;top:1060px;width:440px;height:330px"></div>
  <div class="abs disc-label" style="left:110px;top:1160px;width:240px">PRINCIPAL<br>RESIDENCE</div>
  <div class="abs icon-ph" style="left:178px;top:1296px;width:80px;height:80px" role="img" aria-label="House icon"></div>
  <div class="abs pct-disc" style="left:350px;top:1126px;width:160px;height:160px">32%</div>
  <div class="abs rank" style="left:66px;top:1044px">1st</div>
  <div class="abs rank-tag" style="left:20px;top:1108px">Largest assets</div>
  <p class="abs detail" style="left:72px;top:1430px"><span class="blue">Median value</span><br>in principle residence :</p>
  <div class="abs num" style="left:388px;top:1456px;font-size:46px">$349,000</div>
  <p class="abs detail" style="left:72px;top:1538px"><span class="blue">Median Mortgage value</span><br>of principle residence :</p>
  <div class="abs num" style="left:388px;top:1566px;font-size:46px">$190,000</div>

  <div class="abs disc" style="left:770px;top:1040px;width:380px;height:260px"></div>
  <div class="abs" style="left:690px;top:1080px;width:110px;height:130px;background:#1c1c1c;border-radius:50px 50px 10px 10px" role="img" aria-label="Silhouette of an elderly couple"></div>
  <div class="abs disc-label" style="left:820px;top:1084px;width:200px;font-size:46px">PRIVATE<br>PENSIONS</div>
  <div class="abs pct-disc" style="left:1000px;top:1110px;width:160px;height:160px;font-size:46px">29.2%</div>
  <div class="abs rank" style="left:968px;top:990px;font-size:46px">2nd</div>
  <div class="abs rank-tag" style="left:932px;top:1038px">Largest assets</div>

  <div class="abs frame" style="left:628px;top:1294px;width:560px;height:196px"></div>
  <div class="abs habit" style="left:732px;top:1350px"><span class="num">48%</span><p>Canadian<br><span class="blue">DO NOT SAVE or INVEST</span><br>at all</p></div>
  <div class="abs frame" style="left:628px;top:1504px;width:560px;height:196px"></div>
  <div class="abs habit" style="left:742px;top:1560px"><span class="num">54%</span><p>Canadian<br><span class="blue">DO NOTBUDGET</span><br>regularly</p></div>

  <section class="abs debts" aria-label="Debts"></section>
  <h2 class="abs section-title" style="left:44px;top:1736px;font-size:64px">DEBTS</h2>
  <div class="abs rule" style="left:44px;top:1800px;width:150px;height:3px"></div>
  <p class="abs stat-line" style="left:44px;top:1814px;font-size:30px"><span class="blue">Debt</span> to Disposable income ratio average :</p>
  <div class="abs num" style="left:560px;top:1808px;font-size:40px">172.1</div>
  <p class="abs" style="left:44px;top:1866px;font-size:18px;color:var(--wine)">Type of Borrowing</p>
  <p class="abs borrow-label" style="left:44px;top:1898px">Flexible Rate</p>
  <div class="abs borrow-bar" style="left:194px;top:1898px;width:326px"></div>
  <p class="abs borrow-pct" style="left:528px;top:1900px">74%</p>
  <p class="abs borrow-label" style="left:64px;top:1930px">Variable</p>
  <div class="abs borrow-bar" style="left:194px;top:1930px;width:72px"></div>
  <p class="abs borrow-pct" style="left:276px;top:1932px">21%</p>
  <p class="abs borrow-label" style="left:64px;top:1962px">Blended</p>
  <div class="abs borrow-bar" style="left:194px;top:1962px;width:14px"></div>
  <p class="abs borrow-pct" style="left:218px;top:1964px">5%</p>
  <div class="abs divider" style="left:668px;top:1768px;width:2px;height:220px"></div>
  <p class="abs stat-line" style="left:692px;top:1834px;line-height:1.05">The average<br><span class="blue">borrowing rate</span><br>for Canadian mortgages :</p>
  <div class="abs num" style="left:1020px;top:1874px;font-size:58px">2.94%</div>

  <div class="abs people-icons" role="img" aria-label="Three person icons, one highlighted in blue"></div>
  <p class="abs loss-text" style="left:44px;top:2212px">1 in 3 Canadians have <span class="blue" style="font-size:38px">LOST</span></p>
  <p class="abs loss-text" style="left:44px;top:2280px">at least <span class="num" style="font-size:66px;vertical-align:-10px">20%</span> in one year</p>
  <div class="abs" style="left:478px;top:2046px;width:3px;height:320px;background:var(--teal)"></div>
  <div class="abs loss-row" style="left:560px;top:2080px">
    <span class="num">51%</span>
    <p class="loss-text" style="line-height:1.05">of Canadians took <span class="blue" style="font-size:38px">NO ACTION</span><br>after losing at least <span class="num" style="font-size:32px">20%</span> in one year.</p>
  </div>
  <div class="abs loss-row" style="left:560px;top:2228px">
    <span class="num">22%</span>
    <p class="loss-text" style="line-height:1.15">of those people either<br><span class="blue" style="font-size:36px">HIRED, or FIRED</span> an advisor.</p>
  </div>

  <section class="abs advice" aria-label="Financial advice landscape"></section>
  <div class="abs advice-foot"></div>
  <div class="abs advisor-art" role="img" aria-label="Illustration of an advisor in a suit reading a blue folder beside a Canadian flag"></div>
  <h2 class="abs head" style="left:450px;top:2432px;font-size:62px">FINANCIAL ADVICE LANDSCAPE</h2>
  <p class="abs advice-label" style="left:456px;top:2546px">Number of households :</p>
  <div class="abs advice-value" style="left:790px;top:2536px">13,300,000</div>
  <p class="abs advice-label" style="left:456px;top:2648px">Households with advisors :</p>
  <div class="abs advice-value" style="left:790px;top:2638px">5,300,000 (38%)</div>
  <p class="abs advice-label" style="left:456px;top:2746px;line-height:1.5">Households <span class="blue">dissatisfied</span><br>with existing advisors :</p>
  <div class="abs advice-value" style="left:764px;top:2784px;color:var(--blue)">1,100,000 (20.7%)</div>

  <div class="abs brand"><i></i>Ledgerly</div>
</main>
</body>
</html>
```